I need a cover for a brochure made

I need a cover for a brochure. The dimensions are 8.25 wide and 5.25 high... I also need a .25 inch bleed outside of those dimensions.

I need it to look like a vintage photo album cover. In big words, I would like it to say "Family". Above it in smaller words "To our Harlow Fairway" ... making it look like the words are gold inlay or something.

I would like it kind of in the style of some of the attached maybe. Just vintage looking.

```html
<!DOCTYPE html>
<html lang="en">
<head>
<meta charset="utf-8">
<title>Family – Brochure Cover</title>
<link rel="stylesheet" href="https://fonts.googleapis.com/css2?family=Bubblegum+Sans&family=Chewy&display=swap">
<style>
  :root {
    --leather: #3d2b22;
    --spine: #22201b;
    --oval: #22201b;
    --gold: #bb9632;
    --spine-accent: #3f2c22;
  }
  html, body {
    margin: 0;
    padding: 0;
    width: 1200px;
    height: 770px;
    overflow: hidden;
    background: var(--leather);
  }
  .cover {
    position: relative;
    width: 1200px;
    height: 770px;
    background: var(--leather);
    overflow: hidden;
  }
  .cover-texture {
    position: absolute;
    inset: 0 0 0 265px;
    background: var(--leather);
  }
  .spine {
    position: absolute;
    left: 0;
    top: 0;
    width: 265px;
    height: 770px;
    background: var(--spine);
  }
  .spine-rule {
    position: absolute;
    left: 130px;
    width: 4px;
    background: var(--spine-accent);
  }
  .spine-rule.upper { top: 95px; height: 216px; }
  .spine-rule.lower { top: 459px; height: 217px; }
  .spine-emblem {
    position: absolute;
    left: 81px;
    top: 332px;
    width: 103px;
    height: 105px;
    background: var(--spine-accent);
    border-radius: 18px;
  }
  .gold-frame {
    position: absolute;
    left: 0;
    top: 0;
  }
  .title-plate {
    position: absolute;
    left: 421px;
    top: 157px;
    width: 614px;
    height: 456px;
    border-radius: 50%;
    background: var(--oval);
  }
  .dedication {
    position: absolute;
    left: 421px;
    width: 614px;
    top: 278px;
    margin: 0;
    text-align: center;
    font-family: "Bubblegum Sans", cursive;
    font-size: 31px;
    font-weight: 400;
    color: var(--gold);
    line-height: 1;
  }
  .headline {
    position: absolute;
    left: 421px;
    width: 614px;
    top: 305px;
    margin: 0;
    text-align: center;
    font-family: "Chewy", cursive;
    font-size: 150px;
    font-weight: 400;
    color: var(--gold);
    line-height: 1;
    letter-spacing: 1px;
  }
</style>
</head>
<body>
  <main class="cover">
    <div class="cover-texture" role="img" aria-label="Subtle tone-on-tone hexagon leather pattern"></div>

    <aside class="spine" role="img" aria-label="Dark spine with faint hexagon pattern">
      <span class="spine-rule upper"></span>
      <span class="spine-emblem" role="img" aria-label="Looped knot ornament"></span>
      <span class="spine-rule lower"></span>
    </aside>

    <svg class="gold-frame" width="1200" height="770" viewBox="0 0 1200 770" aria-hidden="true">
      <g stroke="var(--gold)" stroke-width="2" fill="none">
        <line x1="323" y1="39" x2="323" y2="731"/>
        <line x1="330" y1="39" x2="330" y2="731"/>
        <line x1="353" y1="39" x2="353" y2="731"/>
        <line x1="1110" y1="39" x2="1110" y2="731"/>
        <line x1="1133" y1="39" x2="1133" y2="731"/>
        <line x1="1140" y1="39" x2="1140" y2="731"/>
        <line x1="323" y1="39" x2="1140" y2="39"/>
        <line x1="323" y1="50" x2="1140" y2="50"/>
        <line x1="323" y1="62" x2="1140" y2="62"/>
        <line x1="323" y1="707" x2="1140" y2="707"/>
        <line x1="323" y1="719" x2="1140" y2="719"/>
        <line x1="323" y1="731" x2="1140" y2="731"/>
      </g>
    </svg>

    <div class="title-plate"></div>
    <p class="dedication">To Our Harlow Fairway</p>
    <h1 class="headline">Family</h1>
  </main>
</body>
</html>
```